Business Card Design Project for Electrical Company

We need a business card designed for a new Electrical Company called Dorvel Electrical Solutions, i dont mind if only Dorvel Electrical is used. We are a domestic and commercial Electrical Company that provides a range of Electrical Services. Our Company colours are Fluro Yellow and Black with the Lightning bolt picture attached.I have attached a card that has been made i think it is rather basic and am looking for something more. the font of Dorvel Electrical has been used on our car graphics as well as the lightning bolt. i want to keep them the same so we can brand our business. Some things we want on the front of the card are Dorvel Electrical Solutions, Owen Platt, 0438516274, admin@dorvelelectrical.example, Lic No 58342, Servicing CQ Region. But we want Owens name seperate to the phone number as its the phone number for the office, owen wont be answering the phone so we are thinking we dont want to give that impression. What do you think? with all that if you have complete different font designs please submit what you think would work best. keeping in mind our company name and details as well as coulors.

Industry/Entity Type

Business

```html
<!DOCTYPE html>
<html lang="en">
<head>
<meta charset="utf-8">
<title>Dorvel Electrical Solutions – Business Card</title>
<link rel="stylesheet" href="https://fonts.googleapis.com/css2?family=Saira+Semi+Condensed:wght@400;500;600;700;800&family=Share+Tech+Mono&display=swap">
<style>
  :root {
    --fluro: #cde11c;
    --black: #1c1c1c;
    --ink: #2a2a2a;
    --paper: #f4f4f4;
    --paper-shade: #e2e3e4;
    --stage: #eceeef;
    --white: #ffffff;
    --ghost: #dedfe0;
  }
  * { box-sizing: border-box; margin: 0; padding: 0; }
  html, body {
    width: 1200px; height: 900px; overflow: hidden;
    background: radial-gradient(ellipse at 45% 45%, #ffffff 0%, var(--stage) 70%, #dcdfe1 100%);
    font-family: "Saira Semi Condensed", "Arial Narrow", sans-serif;
  }
  .canvas { position: relative; width: 1200px; height: 900px; }

  .card {
    position: absolute; width: 560px; height: 320px; overflow: hidden;
    box-shadow: 0 10px 28px rgba(0,0,0,.18), 0 2px 4px rgba(0,0,0,.12);
  }
  .card-bg { position: absolute; inset: 0; }

  /* FRONT */
  .card--front { left: 590px; top: 70px; background: var(--black); }
  .brand {
    position: absolute; left: 120px; top: 52px; width: 280px;
    color: var(--fluro); font-weight: 800; text-transform: uppercase;
    font-size: 34px; line-height: 0.95; letter-spacing: 0.5px;
  }
  .licence {
    position: absolute; left: 38px; top: 248px;
    display: flex; align-items: center; gap: 10px;
    color: var(--white); font-weight: 500; font-style: italic;
    font-size: 14px; letter-spacing: 1px;
  }
  .rule { display: block; width: 38px; height: 2px; background: var(--white); }
  .person {
    position: absolute; right: 34px; top: 168px; text-align: left;
  }
  .person-name {
    font-weight: 800; font-size: 24px; color: var(--black);
    text-transform: uppercase; letter-spacing: 0.5px; line-height: 1;
  }
  .person-role {
    font-weight: 500; font-size: 13px; color: var(--fluro);
    text-transform: uppercase; letter-spacing: 0.5px; margin-top: 2px;
  }
  .contact {
    position: absolute; right: 34px; top: 226px; text-align: right;
    color: var(--ink);
  }
  .service-area {
    font-weight: 500; font-size: 15px; text-transform: uppercase;
    line-height: 1.1; letter-spacing: 0.5px; margin-bottom: 10px;
  }
  .contact-line {
    display: flex; justify-content: flex-end; align-items: center; gap: 8px;
    font-family: "Share Tech Mono", monospace; font-size: 15px; line-height: 1.35;
  }
  .contact-line svg { width: 16px; height: 14px; fill: var(--ink); }

  /* BACK */
  .card--back { left: 70px; top: 480px; background: var(--paper); }
  .ghost-name {
    position: absolute; left: 170px; top: 30px; width: 300px;
    color: var(--ghost); font-weight: 800; font-size: 40px; line-height: 0.95;
    text-transform: uppercase;
  }
  .services {
    position: absolute; list-style: none;
    color: var(--ink); font-weight: 500; font-size: 18px;
    text-transform: uppercase; line-height: 1.3; letter-spacing: 0.3px;
  }
  .services--left { left: 48px; top: 28px; }
  .services--right { left: 300px; top: 88px; }
  .services li { display: flex; align-items: center; gap: 12px; }
  .check {
    width: 12px; height: 12px; flex: none;
    background:
      linear-gradient(var(--fluro), var(--fluro)) 0 0 / 6px 6px no-repeat,
      linear-gradient(var(--fluro), var(--fluro)) 6px 6px / 6px 6px no-repeat;
  }
  .tagline {
    position: absolute; left: 0; right: 0; top: 250px;
    display: flex; justify-content: center; align-items: center; gap: 18px;
    color: var(--white); font-weight: 600; font-style: italic;
    font-size: 20px; letter-spacing: 6px; text-transform: uppercase;
  }
  .tagline .rule { width: 46px; }
</style>
</head>
<body>
<main class="canvas">

  <section class="card card--front" aria-label="Business card front">
    <svg class="card-bg" viewBox="0 0 560 320" preserveAspectRatio="none" aria-hidden="true">
      <defs>
        <linearGradient id="paperFade" x1="0" y1="0" x2="1" y2="1">
          <stop offset="0" stop-color="#ffffff"/>
          <stop offset="1" stop-color="#dfe0e1"/>
        </linearGradient>
      </defs>
      <path d="M560,84 C420,96 282,188 226,320 L252,320 C304,204 432,114 560,102 Z" fill="var(--fluro)"/>
      <path d="M560,102 C432,114 304,204 252,320 L560,320 Z" fill="url(#paperFade)"/>
    </svg>

    <div class="brand">Dorvel Electrical Solutions</div>

    <div class="licence"><span class="rule"></span>LIC. Nº 58342<span class="rule"></span></div>

    <div class="person">
      <div class="person-name">Owen Platt</div>
      <div class="person-role">Licensed Electrician</div>
    </div>

    <div class="contact">
      <div class="service-area">Servicing CQ<br>Region</div>
      <div class="contact-line">043 851 6274
        <svg viewBox="0 0 16 14" aria-hidden="true"><path d="M1 4 C1 1 15 1 15 4 L15 6 L11 6 L11 4 L5 4 L5 6 L1 6 Z M4 7 L12 7 L14 13 L2 13 Z"/></svg>
      </div>
      <div class="contact-line">admin@dorvelelectrical.example
        <svg viewBox="0 0 16 14" aria-hidden="true"><path d="M1 2 L15 2 L15 12 L1 12 Z M2 3 L8 8 L14 3 Z" fill-rule="evenodd"/></svg>
      </div>
    </div>
  </section>

  <section class="card card--back" aria-label="Business card back">
    <svg class="card-bg" viewBox="0 0 560 320" preserveAspectRatio="none" aria-hidden="true">
      <defs>
        <linearGradient id="backPaper" x1="0" y1="0" x2="0" y2="1">
          <stop offset="0" stop-color="#ffffff"/>
          <stop offset="1" stop-color="#e9eaeb"/>
        </linearGradient>
      </defs>
      <rect width="560" height="212" fill="url(#backPaper)"/>
      <path d="M0,212 L140,212 L152,226 L164,212 L560,212 L560,320 L0,320 Z" fill="var(--black)"/>
    </svg>

    <div class="ghost-name">Dorvel Electrical Solutions</div>

    <ul class="services services--left">
      <li><span class="check"></span>Light &amp; Power</li>
      <li><span class="check"></span>TV &amp; Data</li>
      <li><span class="check"></span>Test &amp; Tagging</li>
      <li><span class="check"></span>Residencial</li>
    </ul>
    <ul class="services services--right">
      <li><span class="check"></span>Renovations</li>
      <li><span class="check"></span>Design &amp; Installation</li>
      <li><span class="check"></span>Air Con Installation</li>
      <li><span class="check"></span>Smoke Detectors</li>
    </ul>

    <div class="tagline"><span class="rule"></span>Lightning up CQ !<span class="rule"></span></div>
  </section>

</main>
</body>
</html>
```